Need Bold, Hip Card for Concert Ticket Website Gleaming Passes!

Hi there! I am putting together a business/website that sells event tickets (mostly concerts, but also some sports and theater). Think SeatNook, but much smaller. The site is called Gleaming Passes. I have a new logo (attached, with black/red/white color scheme), and am looking for a modern/cool/original business card design. Note that I am thinking of having the card itself in the shape of a ticket (die cut), so you may want to keep that in mind when designing, but I'm not set on that. I'm also open to alternative card sizes, thicknesses, glossy, spot UV, etc. in order to stand out. I'm attaching a potential die cut template and a sample card using that template in case you want to work with that.
Target Market(s)
Music fans, people that like going to see live events
Industry/Entity Type
Entertainment
Contact Information for Business Card
Information that I'd like to have:
website address - www.gleamingpasses.example
phone number: 1-833-5GLEAMNG (532-6264)
my name - Wendel Pike

```html
<!DOCTYPE html>
<html lang="en">
<head>
<meta charset="utf-8">
<title>Gleaming Passes – Business Card</title>
<link rel="stylesheet" href="https://fonts.googleapis.com/css2?family=Arimo:wght@400;700&display=swap">
<style>
  :root {
    --backdrop: #2b2b2b;
    --ticket-red: #8c0a0a;
    --ticket-red-deep: #7a0707;
    --paper: #f1f1f1;
    --ink: #111111;
    --white: #ffffff;
  }
  * { margin: 0; padding: 0; box-sizing: border-box; }
  html, body { width: 1200px; height: 1000px; overflow: hidden; }
  body {
    background: var(--backdrop);
    font-family: "Arimo", Arial, sans-serif;
    position: relative;
  }
  .card { position: absolute; width: 711px; }
  .card-shape { position: absolute; left: 0; top: 0; }
  .card-front { left: 247px; top: 85px; height: 398px; }
  .card-back { left: 247px; top: 520px; height: 408px; }

  .front-band {
    position: absolute; left: 0; top: 93px; width: 711px; height: 205px;
    background: var(--paper);
    box-shadow: 0 4px 8px rgba(0,0,0,.35);
  }
  .brand-name {
    position: absolute; left: 0; right: 0; top: 68px;
    text-align: center;
    font-weight: 700; font-size: 54px; letter-spacing: 2px;
    color: var(--ticket-red);
    text-transform: uppercase;
  }
  .front-url {
    position: absolute; left: 0; right: 0; top: 180px;
    text-align: center;
    font-weight: 700; font-size: 18px; color: var(--ink);
  }

  .logo-panel {
    position: absolute; left: 49px; top: 59px; width: 255px; height: 256px;
    background: var(--paper);
    box-shadow: 0 4px 10px rgba(0,0,0,.4);
    display: flex; align-items: center; justify-content: center;
  }
  .logo-panel .brand-name {
    position: static; font-size: 27px; letter-spacing: 1px; line-height: 1.15;
  }
  .holder-name {
    position: absolute; left: 343px; top: 108px;
    font-size: 50px; font-weight: 400; font-variant: small-caps;
    color: var(--white); letter-spacing: 1px;
  }
  .contact-list { position: absolute; left: 341px; top: 170px; list-style: none; }
  .contact-item {
    display: flex; align-items: center; gap: 8px;
    height: 32px; margin-bottom: 9px;
    font-weight: 700; font-size: 17px; color: var(--white);
    white-space: nowrap;
  }
  .contact-icon { width: 32px; height: 32px; flex: none; }
</style>
</head>
<body>

<section class="card card-front" aria-label="Business card front">
  <svg class="card-shape" width="711" height="398" viewBox="0 0 711 398">
    <defs>
      <clipPath id="front-outline">
        <path d="M38 0H673A38 38 0 0 0 711 38V360A38 38 0 0 0 673 398H38A38 38 0 0 0 0 360V38A38 38 0 0 0 38 0Z"/>
      </clipPath>
    </defs>
    <path fill="var(--ticket-red)" d="M38 0H673A38 38 0 0 0 711 38V360A38 38 0 0 0 673 398H38A38 38 0 0 0 0 360V38A38 38 0 0 0 38 0Z"/>
    <g class="staff" fill="var(--ink)" clip-path="url(#front-outline)">
      <rect x="0" y="10" width="711" height="3"/>
      <rect x="0" y="20" width="711" height="3"/>
      <rect x="0" y="30" width="711" height="3"/>
      <rect x="0" y="40" width="711" height="3"/>
      <rect x="0" y="50" width="711" height="3"/>
      <rect x="0" y="334" width="711" height="3"/>
      <rect x="0" y="344" width="711" height="3"/>
      <rect x="0" y="354" width="711" height="3"/>
      <rect x="0" y="364" width="711" height="3"/>
      <rect x="0" y="374" width="711" height="3"/>
    </g>
  </svg>
  <div class="front-band">
    <p class="brand-name">Gleaming Passes</p>
    <p class="front-url">WWW.GLEAMINGPASSES.EXAMPLE</p>
  </div>
</section>

<section class="card card-back" aria-label="Business card back">
  <svg class="card-shape" width="711" height="408" viewBox="0 0 711 408">
    <defs>
      <clipPath id="back-outline">
        <path d="M38 0H673A38 38 0 0 0 711 38V370A38 38 0 0 0 673 408H38A38 38 0 0 0 0 370V38A38 38 0 0 0 38 0Z"/>
      </clipPath>
    </defs>
    <path fill="var(--ticket-red)" d="M38 0H673A38 38 0 0 0 711 38V370A38 38 0 0 0 673 408H38A38 38 0 0 0 0 370V38A38 38 0 0 0 38 0Z"/>
    <g class="staff" fill="var(--ink)" clip-path="url(#back-outline)">
      <rect x="0" y="344" width="711" height="3"/>
      <rect x="0" y="354" width="711" height="3"/>
      <rect x="0" y="364" width="711" height="3"/>
      <rect x="0" y="374" width="711" height="3"/>
      <rect x="0" y="384" width="711" height="3"/>
    </g>
  </svg>
  <div class="logo-panel">
    <p class="brand-name">Gleaming<br>Passes</p>
  </div>
  <h1 class="holder-name">Wendel Pike</h1>
  <ul class="contact-list">
    <li class="contact-item">
      <svg class="contact-icon" viewBox="0 0 32 32" aria-hidden="true">
        <circle cx="16" cy="16" r="15" fill="var(--white)"/>
        <path fill="var(--ticket-red)" d="M10 8l4 0 1.5 5-2.5 2c1 2.5 2.5 4 5 5l2-2.5 5 1.5v4c0 1-1 2-2 2C14 25 7 18 7 10c0-1 1-2 3-2z"/>
      </svg>
      <span>1-833-5GLEAMNG (532-6264)</span>
    </li>
    <li class="contact-item">
      <svg class="contact-icon" viewBox="0 0 32 32" aria-hidden="true">
        <circle cx="16" cy="16" r="15" fill="var(--white)"/>
        <rect x="8" y="10" width="16" height="12" fill="var(--ticket-red)"/>
        <path d="M8 10l8 7 8-7" fill="none" stroke="var(--white)" stroke-width="1.6"/>
      </svg>
      <span>INFO@GLEAMINGPASSES.EXAMPLE</span>
    </li>
    <li class="contact-item">
      <svg class="contact-icon" viewBox="0 0 32 32" aria-hidden="true">
        <circle cx="16" cy="16" r="15" fill="var(--white)"/>
        <g fill="none" stroke="var(--ticket-red)" stroke-width="1.6">
          <circle cx="16" cy="16" r="10"/>
          <ellipse cx="16" cy="16" rx="4.5" ry="10"/>
          <path d="M6 16h20M8 11h16M8 21h16"/>
        </g>
      </svg>
      <span>WWW.GLEAMINGPASSES.EXAMPLE</span>
    </li>
  </ul>
</section>

</body>
</html>
```